Design a Professional Business Card for Velmora Arcs

Design a business card for Velmora Arcs, we are a National Sport Court Company.

West Region Address: 4175 Quill Harbor Ln, Suite #215 Englewood, Colorado 80467
East Region Address: 3817 Tamsin Rd E, Bradenton, Florida 34583

Target Market(s)

High End Residential & Institutional Clients

Industry/Entity Type

Design & Construction

Contact Information for Business Card

Logo/Brand/Colors/ name, number (provided in comments)

Requirements
Must have
• Colors only provided in logo
Should not have
• Any other colors not in existing logo (attached)

```html
<!DOCTYPE html>
<html lang="en">
<head>
<meta charset="utf-8">
<title>Velmora Arcs – Business Card</title>
<link href="https://fonts.googleapis.com/css2?family=Michroma&family=Poppins:wght@300;400;600;700&display=swap" rel="stylesheet">
<style>
  :root {
    --navy: #1d3461;
    --navy-deep: #192d55;
    --green: #036634;
    --band: #e2e5eb;
    --card: #ffffff;
    --mark: #c9d0dc;
  }
  * { margin: 0; padding: 0; box-sizing: border-box; }
  html, body { width: 1200px; height: 1200px; overflow: hidden; background: var(--navy); }
  .canvas { position: relative; width: 1200px; height: 1200px; background: var(--navy); font-family: "Poppins", sans-serif; }
  .card-shadow { position: absolute; background: var(--navy-deep); border-radius: 4px; }
  .card { position: absolute; left: 298px; width: 604px; height: 345px; background: var(--card); border-radius: 14px; overflow: hidden; }
  .card--front { top: 218px; background: linear-gradient(180deg, #f6f7f8 0%, #ffffff 60%, #f5f6f7 100%); }
  .card--back { top: 637px; }
  .crop { position: absolute; width: 22px; height: 22px; border-color: var(--mark); border-style: solid; border-width: 0; }
  .crop--tl { border-right-width: 1px; border-bottom-width: 1px; }
  .crop--tr { border-left-width: 1px; border-bottom-width: 1px; }
  .crop--bl { border-right-width: 1px; border-top-width: 1px; }
  .crop--br { border-left-width: 1px; border-top-width: 1px; }
  .card-art { position: absolute; inset: 0; }
  .wordmark { position: absolute; left: 350px; top: 222px; width: 215px; font-weight: 700; font-size: 36px; line-height: 40px; letter-spacing: 3px; color: var(--navy); text-align: right; }
  .person-name { position: absolute; left: 37px; top: 32px; font-family: "Michroma", sans-serif; font-size: 17px; color: var(--navy); letter-spacing: 0.5px; }
  .person-title { position: absolute; left: 37px; width: 321px; top: 57px; text-align: right; font-size: 11px; letter-spacing: 2px; color: var(--green); }
  .contact-list { position: absolute; left: 40px; top: 114px; list-style: none; }
  .contact-item { display: flex; align-items: center; height: 23px; font-size: 16.5px; font-weight: 300; color: var(--navy); }
  .contact-item svg { width: 16px; height: 16px; margin-right: 15px; flex: none; }
  .address-block { position: absolute; left: 40px; top: 226px; display: flex; }
  .address-pin { width: 16px; height: 20px; margin-right: 6px; }
  .address-text { border-left: 1px solid var(--mark); padding-left: 10px; font-size: 12.5px; line-height: 14px; color: var(--navy); }
  .address-heading { font-weight: 600; color: var(--green); font-size: 13px; line-height: 16px; }
  .address-lines + .address-heading { margin-top: 4px; }
</style>
</head>
<body>
<main class="canvas">
  <div class="card-shadow" style="left:292px;top:226px;width:634px;height:360px;"></div>
  <div class="card-shadow" style="left:292px;top:645px;width:634px;height:360px;"></div>

  <span class="crop crop--tl" style="left:276px;top:196px;"></span>
  <span class="crop crop--tr" style="left:902px;top:196px;"></span>
  <span class="crop crop--bl" style="left:276px;top:562px;"></span>
  <span class="crop crop--br" style="left:902px;top:562px;"></span>
  <span class="crop crop--tl" style="left:276px;top:615px;"></span>
  <span class="crop crop--tr" style="left:902px;top:615px;"></span>
  <span class="crop crop--bl" style="left:276px;top:982px;"></span>
  <span class="crop crop--br" style="left:902px;top:982px;"></span>

  <section class="card card--front" aria-label="Card front">
    <svg class="card-art" viewBox="0 0 604 345" aria-hidden="true">
      <path d="M0 124 C30 124 45 112 60 84 C85 40 130 31 185 31 C250 31 290 70 345 120 C420 158 540 150 604 120 L604 235 C540 205 420 200 345 240 C290 285 250 314 185 314 C130 314 85 300 60 258 C45 230 30 220 0 220 Z" fill="var(--band)"/>
      <circle cx="185" cy="171" r="98" fill="var(--navy)"/>
    </svg>
    <div class="wordmark">VELMORA<br>ARCS</div>
  </section>

  <section class="card card--back" aria-label="Card back">
    <svg class="card-art" viewBox="0 0 604 345" aria-hidden="true">
      <circle cx="449" cy="225" r="108" fill="var(--green)"/>
    </svg>
    <h1 class="person-name">DORIAN M. HALVORSEN, ASLA</h1>
    <p class="person-title">CEO &amp; FOUNDER</p>
    <ul class="contact-list">
      <li class="contact-item"><svg viewBox="0 0 16 16"><path d="M5 2h9v12H5" fill="none" stroke="var(--navy)" stroke-width="1.6"/><path d="M1 8h8M6 5l3 3-3 3" fill="none" stroke="var(--navy)" stroke-width="1.6"/></svg>(303) 555-0147</li>
      <li class="contact-item"><svg viewBox="0 0 16 16"><path d="M3 2l3 0 1 3-2 1.5c1 2 2.5 3.5 4.5 4.5L11 9l3 1v3c-6 1-12-5-11-11z" fill="var(--navy)"/></svg>1-800-555-0193</li>
      <li class="contact-item"><svg viewBox="0 0 16 16"><rect x="2" y="4" width="12" height="8" fill="var(--navy)"/><path d="M2 4l6 5 6-5" fill="none" stroke="#fff" stroke-width="1.2"/></svg>dorian@velmoraarcs.com</li>
      <li class="contact-item"><svg viewBox="0 0 16 16"><circle cx="8" cy="8" r="6" fill="none" stroke="var(--navy)" stroke-width="1.4"/><ellipse cx="8" cy="8" rx="2.6" ry="6" fill="none" stroke="var(--navy)" stroke-width="1.2"/><path d="M2 8h12" stroke="var(--navy)" stroke-width="1.2"/></svg>www.velmoraarcs.com</li>
    </ul>
    <div class="address-block">
      <svg class="address-pin" viewBox="0 0 16 20"><path d="M8 1a6 6 0 0 0-6 6c0 4.5 6 12 6 12s6-7.5 6-12a6 6 0 0 0-6-6z" fill="var(--navy)"/><circle cx="8" cy="7" r="2.2" fill="#fff"/></svg>
      <div class="address-text">
        <p class="address-heading">West Region Address</p>
        <p class="address-lines">4175 Quill Harbor Ln, Suite<br>#215 Englewood, Colorado 80467</p>
        <p class="address-heading">East Region Address</p>
        <p class="address-lines">3817 Tamsin Rd E, Bradenton,<br>Florida 34583</p>
      </div>
    </div>
  </section>
</main>
</body>
</html>
```